Vital Spark Electrical in need of a business card design

We need a new business card designed for our electrical business. We have a logo already which I will attach below.
Would like the business card to be..
-BLACK background preferably, possibly white back ground behind logo if colours clash.
-White & Blue (logo blue) text
Something that makes the logo pop, & a modern look. Possibly minimal clean format.

REQUIRE:
-Logo on front & back

TEXT TO INCLUDE (ON ONE SIDE):

Tom Harlow
Director/Electrician
M: 0417 365 208
E:info@vitalsparkelectrical-example.com.au
W:www.vitalsparkelectrical-example.com.au
R.E.C 57318

Custom/New Homes
Renovations
Commercial Office/Shop Fit-outs
Communications & Security Cameras
Electric Vehicle Chargers
Airconditioning
Updates

Requirements
Nice to have
• Possibly even lighten the grey shades for the words 'Vital' & 'Spark' to be more easily read on a black background.

```html
<!DOCTYPE html>
<html lang="en">
<head>
<meta charset="utf-8">
<title>Vital Spark Electrical – Business Card</title>
<link rel="stylesheet" href="https://fonts.googleapis.com/css2?family=Montserrat:wght@500;600;700&family=Questrial&display=swap">
<style>
  :root {
    --stage: #2a2a2b;
    --card: #1f1f20;
    --blue: #1aa6e0;
    --blue-deep: #0f9ad6;
    --grey: #5d6670;
    --logo-grey: #aab3bc;
    --white: #f2f4f6;
    --muted: #d9dde1;
  }
  * { box-sizing: border-box; margin: 0; padding: 0; }
  html, body { width: 1200px; height: 900px; overflow: hidden; }
  body {
    background: var(--stage);
    font-family: "Questrial", "Helvetica Neue", Arial, sans-serif;
    color: var(--white);
    position: relative;
  }
  .card {
    position: absolute;
    left: 250px;
    width: 700px;
    height: 400px;
    background: var(--card);
    border-radius: 18px;
    overflow: hidden;
    box-shadow: 0 10px 28px rgba(0,0,0,.45);
  }
  .card--front { top: 40px; }
  .card--back { top: 460px; }

  .brand {
    display: flex;
    align-items: center;
    gap: 14px;
  }
  .brand__square {
    width: 34px;
    height: 34px;
    background: var(--blue);
    border-radius: 4px;
  }
  .brand__name {
    font-family: "Montserrat", Arial, sans-serif;
    font-weight: 600;
    color: var(--logo-grey);
    letter-spacing: .5px;
  }

  /* Front */
  .card--front .brand {
    position: absolute;
    top: 110px;
    left: 0; right: 0;
    justify-content: center;
  }
  .card--front .brand__name { font-size: 34px; }
  .services {
    position: absolute;
    top: 215px;
    left: 0; right: 0;
    text-align: center;
  }
  .services__title {
    font-family: "Montserrat", Arial, sans-serif;
    font-weight: 700;
    font-size: 17px;
    color: var(--blue);
    letter-spacing: .5px;
    display: inline-block;
    padding-bottom: 8px;
    border-bottom: 1px solid var(--grey);
    margin-bottom: 12px;
  }
  .services__row {
    font-size: 15px;
    color: var(--white);
    line-height: 1.75;
  }
  .services__sep { color: var(--blue); padding: 0 6px; }

  /* Back */
  .card--back .brand {
    position: absolute;
    top: 92px;
    left: 50px;
  }
  .card--back .brand__name { font-size: 24px; }
  .person {
    position: absolute;
    top: 70px;
    right: 50px;
    text-align: right;
  }
  .person__name {
    font-family: "Montserrat", Arial, sans-serif;
    font-weight: 700;
    font-size: 26px;
    color: var(--blue);
    text-transform: uppercase;
  }
  .person__role { font-size: 17px; color: var(--white); margin-top: 2px; }
  .rule {
    position: absolute;
    height: 1px;
    background: var(--blue-deep);
    opacity: .7;
  }
  .rule--top { top: 150px; left: 50px; right: 50px; }
  .rule--contact { top: 262px; left: 50px; width: 300px; }
  .contact {
    position: absolute;
    top: 276px;
    left: 50px;
    list-style: none;
    font-size: 15px;
    line-height: 1.85;
  }
  .contact__item { display: flex; align-items: center; gap: 10px; }
  .contact__icon { width: 13px; height: 13px; flex: none; }
  .corner {
    position: absolute;
    inset: 0;
    width: 700px;
    height: 400px;
  }
  .corner__licence {
    font-family: "Questrial", Arial, sans-serif;
    font-size: 20px;
    fill: var(--white);
  }
</style>
</head>
<body>

  <section class="card card--front" aria-label="Card front">
    <div class="brand">
      <span class="brand__square"></span>
      <span class="brand__name">Vital Spark Electrical</span>
    </div>
    <div class="services">
      <h2 class="services__title">OUR SERVICES</h2>
      <p class="services__row">Custom/New Homes<span class="services__sep">|</span>Renovations<span class="services__sep">|</span>Commercial Office/Shop Fit-outs</p>
      <p class="services__row">Communications &amp; Security Cameras<span class="services__sep">|</span>Electric Vehicle Chargers<span class="services__sep">|</span>Airconditioning</p>
    </div>
  </section>

  <section class="card card--back" aria-label="Card back">
    <svg class="corner" viewBox="0 0 700 400" aria-hidden="false">
      <polygon points="700,150 700,400 300,400" fill="#5d6670"/>
      <polygon points="700,178 700,400 360,400" fill="#1aa6e0"/>
      <text class="corner__licence" x="0" y="0" transform="translate(548 352) rotate(-33)">R.E.C 57318</text>
    </svg>

    <div class="brand">
      <span class="brand__square"></span>
      <span class="brand__name">Vital Spark Electrical</span>
    </div>

    <div class="person">
      <h1 class="person__name">Tom Harlow</h1>
      <p class="person__role">Director/Electrician</p>
    </div>

    <div class="rule rule--top"></div>
    <div class="rule rule--contact"></div>

    <ul class="contact">
      <li class="contact__item">
        <svg class="contact__icon" viewBox="0 0 12 12"><rect x="2.5" y="0.5" width="7" height="11" rx="1.5" fill="none" stroke="#1aa6e0" stroke-width="1.2"/><circle cx="6" cy="9.5" r=".8" fill="#1aa6e0"/></svg>
        <span>0417 365 208</span>
      </li>
      <li class="contact__item">
        <svg class="contact__icon" viewBox="0 0 12 12"><rect x="0.5" y="2" width="11" height="8" rx="1" fill="#1aa6e0"/><path d="M1 2.5 L6 6.5 L11 2.5" fill="none" stroke="#1f1f20" stroke-width="1"/></svg>
        <span>info@vitalsparkelectrical-example.com.au</span>
      </li>
      <li class="contact__item">
        <svg class="contact__icon" viewBox="0 0 12 12"><circle cx="6" cy="6" r="5.3" fill="none" stroke="#1aa6e0" stroke-width="1.2"/><ellipse cx="6" cy="6" rx="2.2" ry="5.3" fill="none" stroke="#1aa6e0" stroke-width="1"/><line x1="0.7" y1="6" x2="11.3" y2="6" stroke="#1aa6e0" stroke-width="1"/></svg>
        <span>www.vitalsparkelectrical-example.com.au</span>
      </li>
    </ul>
  </section>

</body>
</html>
```